Bref créative
Tamsel Briar Gifts
wrapped with care, just for you!
Bright & Fun-filled
Marta Fowler
Owner
no address - online only
fowler@tamselbriargifts.example
www.tamselbriargifts.example
I would like my logo on the front in white background.
I would like my logo in black background.

```html
<!DOCTYPE html>
<html lang="en">
<head>
<meta charset="utf-8">
<title>Tamsel Briar Gifts – Business Cards</title>
<link href="https://fonts.googleapis.com/css2?family=Open+Sans:ital,wght@0,400;0,600;1,400&display=swap" rel="stylesheet">
<style>
  :root {
    --stage: #1c1c1c;
    --stage-light: #2a2a2a;
    --floor: #0c0c0c;
    --card-white: #ffffff;
    --card-black: #0a0a0a;
    --magenta: #b0197e;
    --magenta-soft: #d23a9c;
    --orange: #d98a2a;
    --ink: #333333;
    --grey: #777777;
  }
  * { box-sizing: border-box; margin: 0; padding: 0; }
  html, body { width: 1200px; height: 770px; overflow: hidden; }
  body {
    font-family: "Open Sans", Arial, sans-serif;
    background: linear-gradient(180deg, var(--stage-light) 0%, var(--stage) 70%, var(--floor) 100%);
    position: relative;
  }
  .floor-band { position: absolute; left: 0; right: 0; top: 700px; height: 70px; background: var(--floor); }
  .card {
    position: absolute; width: 505px; height: 275px;
    box-shadow: 0 6px 18px rgba(0,0,0,.7);
    overflow: hidden;
  }
  .card--white { background: var(--card-white); }
  .card--black { background: var(--card-black); }
  .card--front-a { left: 92px; top: 100px; }
  .card--back-a  { left: 617px; top: 100px; }
  .card--front-b { left: 92px; top: 405px; }
  .card--back-b  { left: 617px; top: 405px; }

  .bar-top { position: absolute; left: 0; right: 0; top: 14px; height: 9px; background: var(--magenta); }
  .bar-bottom { position: absolute; left: 0; right: 0; bottom: 14px; height: 4px; background: var(--magenta); }
  .bar-top-thin { position: absolute; left: 0; right: 0; top: 0; height: 5px; background: var(--magenta); }

  .logo { position: absolute; text-align: left; }
  .logo-name {
    display: flex; align-items: center; gap: 8px;
    color: var(--magenta); font-weight: 600; font-size: 22px; white-space: nowrap;
  }
  .logo-dot { width: 13px; height: 13px; border-radius: 50%; background: var(--magenta); flex: none; }
  .logo--on-dark .logo-name { color: var(--magenta-soft); }
  .logo--on-dark .logo-dot { background: var(--magenta-soft); }
  .tagline { color: var(--orange); font-style: italic; font-size: 10px; margin-top: 4px; padding-left: 21px; white-space: nowrap; }

  .person { position: absolute; right: 40px; text-align: left; }
  .person-name { color: var(--magenta); font-size: 18px; white-space: nowrap; }
  .person-role { color: var(--ink); font-size: 11px; padding-left: 40px; }

  .contacts { position: absolute; list-style: none; font-size: 11px; color: var(--ink); line-height: 1.9; white-space: nowrap; }
  .contacts b { color: var(--magenta); font-weight: 600; margin-right: 3px; }

  .ribbon { position: absolute; border-radius: 40% 60% 30% 70%; }
  .ribbon--light { background: radial-gradient(ellipse at center, rgba(176,25,126,.28), rgba(176,25,126,0) 70%); }
  .ribbon--dark { background: radial-gradient(ellipse at center, rgba(120,90,110,.55), rgba(74,58,68,0) 70%); }

  .web { position: absolute; font-size: 10px; color: var(--grey); white-space: nowrap; }
  .web b { color: var(--magenta-soft); font-weight: 600; margin-right: 3px; }
</style>
</head>
<body>
  <div class="floor-band"></div>

  <section class="card card--white card--front-a">
    <div class="bar-top"></div>
    <div class="bar-bottom"></div>
    <div class="logo" style="left:22px; top:122px;">
      <div class="logo-name"><span class="logo-dot"></span>Tamsel Briar Gifts</div>
      <div class="tagline">wrapped with care, just for you!</div>
    </div>
    <div class="person" style="top:40px;">
      <div class="person-name">Marta Fowler</div>
      <div class="person-role">Owner</div>
    </div>
    <ul class="contacts" style="left:280px; top:115px;">
      <li><b>P:</b>555-014-2738</li>
      <li><b>E:</b>fowler@tamselbriargifts.example</li>
      <li><b>W:</b>www.tamselbriargifts.example</li>
    </ul>
  </section>

  <section class="card card--black card--back-a">
    <div class="ribbon ribbon--dark" role="img" aria-label="Large ribbon bow decoration" style="left:20px; top:0; width:300px; height:110px;"></div>
    <div class="logo logo--on-dark" style="left:225px; top:140px;">
      <div class="logo-name"><span class="logo-dot"></span>Tamsel Briar Gifts</div>
      <div class="tagline">wrapped with care, just for you!</div>
    </div>
    <div class="web" style="left:22px; bottom:18px;"><b>W:</b>www.tamselbriargifts.example</div>
  </section>

  <section class="card card--white card--front-b">
    <div class="bar-top-thin"></div>
    <div class="logo" style="left:18px; top:72px;">
      <div class="logo-name"><span class="logo-dot"></span>Tamsel Briar Gifts</div>
      <div class="tagline">wrapped with care, just for you!</div>
    </div>
    <div class="person" style="top:50px;">
      <div class="person-name" style="font-size:21px;">Marta Fowler</div>
      <div class="person-role" style="font-size:13px;">Owner</div>
    </div>
    <ul class="contacts" style="left:14px; top:185px;">
      <li><b>P:</b>555-014-2738</li>
      <li><b>E:</b>fowler@tamselbriargifts.example</li>
      <li><b>W:</b>www.tamselbriargifts.example</li>
    </ul>
    <div class="ribbon ribbon--light" role="img" aria-label="Ribbon bow decoration" style="left:340px; top:170px; width:160px; height:95px;"></div>
  </section>

  <section class="card card--black card--back-b">
    <div class="logo logo--on-dark" style="left:165px; top:74px;">
      <div class="logo-name"><span class="logo-dot"></span>Tamsel Briar Gifts</div>
      <div class="tagline">wrapped with care, just for you!</div>
    </div>
    <div class="ribbon ribbon--dark" role="img" aria-label="Ribbon bow decoration" style="left:10px; top:150px; width:170px; height:110px;"></div>
    <div class="web" style="right:22px; bottom:16px;"><b>W:</b>www.tamselbriargifts.example</div>
  </section>
</body>
</html>
```